Website Design for my CNC machine Shop.

I need a new website for my Machining Company.

It can be a simple website that acts more like an "Online Business card" I has to highlight the services I provide and give Companies the confidence to engage my services.

I needs it to be a really modern or even a little futuristic promoting my Company.

I have just moved locations and have renovated the premises and would be great to let everyone know along with a new website.

If you can help with linking it to search engines to help get more exposure that would be great.

It needs to accommodate the three main services I provide which will include capacities of each machine (within that service) and maybe a couple images.
CNC Machining (5-axis, 3-axis)
EDM Wire cutting
3D Metal Printing
Along with home page and Contact page

I have two websites and you can use the txt from either/combination of these.
www.korvanmetalworks.com.au
(no longer do Laser Marking and etching but now do 3D metal Printing)
www.brislotech.com.au

Happy to chat further with the designer

Company logo's provided.

For Images: I am happy to use Pixelgrove and can purchase any images you like
EDM Wire cut
https://www.pixelgrove.com/search/edm-wire-cutting

CNC Machining:
https://www.pixelgrove.com/search/vertical-cnc-machining
Don't use any with engines or motor vehicle parts

3D metal Printing
https://www.pixelgrove.com/search/slm-metal-printing

Target Market(s)

Defence, Aerospace, Medical, HIgh Precision

Industry/Entity Type

Mechanical Engineering

Coding

Coded - Design and coding required

Number of Pages Required

5+ page

Requirements
Must have
• Home page, 3 services, Contacts. Can add image to each of the services

```html
<!DOCTYPE html>
<html lang="en">
<head>
<meta charset="utf-8">
<title>Korvan Precision Machinists</title>
<link href="https://fonts.googleapis.com/css2?family=Montserrat:wght@400;500;600;700&display=swap" rel="stylesheet">
<style>
:root{
  --green:#1c8a4a;
  --ink:#111;
  --grey:#6a6f73;
  --dark:#1b1d1f;
  --white:#fff;
  --footer-bar:#d9d9d9;
}
*{box-sizing:border-box;margin:0;padding:0}
html,body{width:1200px;height:3386px;overflow:hidden;background:var(--white)}
body{font-family:'Montserrat',sans-serif;color:var(--ink);position:relative}
section,header,footer{position:relative;width:1200px;overflow:hidden}
.abs{position:absolute}
.photo{position:absolute}
/* header */
.site-header{height:86px}
.brand{position:absolute;left:26px;top:22px;display:flex;align-items:center;gap:8px}
.brand-name{font-weight:700;font-size:36px;letter-spacing:2px;color:#5f6a70}
.brand-mark{width:10px;height:10px;background:var(--green)}
.phone{position:absolute;right:24px;top:7px;font-size:15px;display:flex;align-items:center;gap:6px}
.nav{position:absolute;right:26px;top:47px;display:flex;align-items:center;gap:32px;font-size:12.5px;font-weight:500}
.nav-cta{background:var(--green);color:#fff;padding:6px 13px}
/* buttons */
.btn{display:inline-flex;align-items:center;justify-content:center;font-size:12.5px;font-weight:500;height:32px;padding:0 9px;border:1px solid var(--ink);color:var(--ink)}
.btn-solid{background:var(--green);border-color:var(--green);color:#fff}
.btn-light{border-color:#fff;color:#fff}
.link-arrow{display:inline-flex;align-items:center;gap:10px;font-size:12.5px;font-weight:500;margin-left:16px}
.actions{display:flex;align-items:center}
/* hero */
.hero{height:571px;background:#2c2f31}
.hero .photo{inset:0;background:radial-gradient(ellipse at 70% 30%,#6b7175 0%,#3a3e41 45%,#1c1e20 100%)}
.hero h1{position:absolute;left:86px;top:145px;width:740px;font-size:42px;font-weight:600;line-height:50px;color:#fff}
.hero p{position:absolute;left:86px;top:312px;width:620px;font-size:21px;line-height:27px;color:#fff}
.hero .actions{position:absolute;left:86px;top:385px;gap:9px}
.hero .btn{width:128px;height:34px}
/* intro */
.intro{height:473px}
.intro h2{position:absolute;left:86px;top:66px;width:470px;font-size:27px;line-height:30px;font-weight:600}
.intro .lead{position:absolute;left:86px;top:174px;width:480px;font-size:12.5px;line-height:19px}
.feature{position:absolute;top:247px;width:240px;font-size:12px;line-height:19px}
.feature h3{font-size:13.5px;font-weight:600;margin-bottom:8px}
.intro .photo{left:635px;top:70px;width:479px;height:375px;background:linear-gradient(160deg,#1d3a78 0%,#3b64a8 40%,#b97a3b 70%,#e7a24a 80%,#1f3b6e 100%)}
/* services */
.services{height:526px}
.services h2{position:absolute;left:86px;top:35px;width:500px;font-size:27px;line-height:30px;font-weight:600}
.services .lead{position:absolute;left:86px;top:112px;width:470px;font-size:12.5px;line-height:19px}
.card{position:absolute;top:209px;width:330px}
.card .photo{position:relative;width:143px;height:85px}
.card h3{font-size:17px;font-weight:500;line-height:18px;margin-top:24px;width:260px}
.card p{font-size:12.5px;line-height:19px;margin-top:12px;width:310px;min-height:57px}
.card .actions{margin-top:20px}
/* quality */
.quality{height:482px}
.quality h2{position:absolute;left:84px;top:72px;width:480px;font-size:27px;line-height:30px;font-weight:600}
.quality .lead{position:absolute;left:86px;top:150px;width:480px;font-size:12.5px;line-height:19px}
.stat{position:absolute;top:225px;width:200px}
.stat strong{display:block;font-size:26px;font-weight:600}
.stat p{font-size:12.5px;line-height:19px;margin-top:8px;width:170px}
.stat .actions{margin-top:24px}
.quality .photo{left:635px;top:33px;width:479px;height:381px;background:radial-gradient(circle at 40% 50%,#b9bbbb 0%,#8b8d8b 55%,#5e605f 100%)}
/* CTA */
.cta{height:272px;background:var(--dark)}
.cta .photo{inset:0;background:linear-gradient(90deg,#2a2c2e 0%,#161819 50%,#2e3133 100%)}
.cta h2{position:absolute;left:230px;top:95px;font-size:26px;font-weight:600;color:#fff}
.cta p{position:absolute;left:232px;top:149px;font-size:12.5px;font-weight:500;color:#fff}
.cta .actions{position:absolute;left:782px;top:113px;gap:17px}
/* stats */
.stats{height:372px}
.stats h2{position:absolute;left:84px;top:87px;width:420px;font-size:27px;line-height:30px;font-weight:600}
.stats .lead{position:absolute;left:86px;top:167px;width:480px;font-size:12.5px;line-height:19px}
.stats .actions{position:absolute;left:86px;top:246px}
.metric{position:absolute;width:220px;height:101px;border-left:2px solid var(--ink);padding-left:6px}
.metric strong{display:block;font-size:50px;font-weight:600;line-height:60px;margin-top:8px}
.metric span{font-size:13.5px;font-weight:600}
/* testimonial */
.testimonial{height:306px;background:#101820}
.testimonial .photo{inset:0;background:radial-gradient(ellipse at 50% 80%,#24404a 0%,#132028 60%,#0a0f13 100%)}
.quote-mark{position:absolute;left:222px;top:40px;font-size:90px;font-weight:700;color:#5a6468;line-height:1}
.testimonial blockquote{position:absolute;left:250px;top:60px;width:700px;text-align:center;font-size:21px;line-height:30px;color:#fff}
.arrow-btn{position:absolute;top:125px;width:58px;height:58px;border:2px solid #fff;border-radius:50%;display:flex;align-items:center;justify-content:center}
.avatar{position:absolute;left:571px;top:142px;width:57px;height:57px;border-radius:50%;background:linear-gradient(#c9ced1,#7e878c)}
.person{position:absolute;left:0;width:1200px;text-align:center;color:#fff;top:212px}
.person strong{display:block;font-size:12.5px;font-weight:700}
.person span{font-size:12px;font-weight:500}
/* footer */
.site-footer{height:243px}
.site-footer .brand{top:38px}
.footer-col{position:absolute;top:45px;font-size:12px;font-weight:500}
.footer-col h4{font-size:13.5px;font-weight:600;margin-bottom:20px}
.footer-col li{list-style:none;margin-bottom:27px}
.footer-col address{font-style:normal;line-height:19px}
.copyright{height:55px;background:var(--footer-bar);text-align:center;font-size:12.5px;font-weight:500;line-height:55px}
</style>
</head>
<body>

<header class="site-header">
  <div class="brand"><span class="brand-name">KORVAN</span><span class="brand-mark"></span></div>
  <div class="phone">
    <svg width="18" height="18" viewBox="0 0 24 24" fill="none" stroke="#111" stroke-width="2"><path d="M5 3h4l2 5-2.5 1.5a11 11 0 0 0 6 6L16 13l5 2v4a2 2 0 0 1-2 2A17 17 0 0 1 3 5a2 2 0 0 1 2-2z"/></svg>
    +61 400 512 874
  </div>
  <nav class="nav">
    <span>HOME</span><span>EDM WIRE CUTTING</span><span>CNC MACHINING</span><span>3D METAL PRINTING</span><span class="nav-cta">CONTACT</span>
  </nav>
</header>

<section class="hero">
  <div class="photo" role="img" aria-label="CNC spindle cutting metal with coolant spraying"></div>
  <h1>We are an innovative&nbsp; company that specialise in technical and creative engineering</h1>
  <p>Our core sectors of expertise are in EDM wire cutting, Laser Etching/Marking and CNC machining.</p>
  <div class="actions"><span class="btn btn-solid">Learn More</span><span class="btn btn-light">Contact Us</span></div>
</section>

<section class="intro">
  <h2>We are an innovative&nbsp; company that specialise in technical and creative engineering.</h2>
  <p class="lead">Our core sectors of expertise are in EDM wire cutting, Laser Etching/Marking and CNC machining. With our combination of highly skilled staff and sophisticated machinery we offer a comprehensive and professional service.</p>
  <div class="feature" style="left:85px"><h3>Precision. Efficiency.</h3>Experience the power of our state-of-the-art machines and expert craftsmanship.</div>
  <div class="feature" style="left:349px"><h3>Precision. Efficiency.</h3>Unlock new pssibilities with our cuttong-edge technologies and exceptional service.</div>
  <div class="photo" role="img" aria-label="Machine tool throwing orange sparks against blue background"></div>
</section>

<section class="services">
  <h2>Unmatched Machining Services for Your Business</h2>
  <p class="lead">Lorem ipsum dolor sit amet, consectetur adipisicing elit, sed do eiusmod tempor incididunt ut labore et dolore magna aliqua. Ut enim ad minim veniam, quis nostrud exercitation ullamco laboris nisi ut aliquip ex ea commodo consequat.</p>

  <article class="card" style="left:86px">
    <div class="photo" role="img" aria-label="EDM wire cutting machine in blue light" style="background:linear-gradient(135deg,#2d4f6e,#7ea3bd,#1e3246)"></div>
    <h3>EDM Wire Cutting: Intricate and Delicate</h3>
    <p>We operate Swiss manufactured Veltrona EDM Machines which are regarded as the Aurelian of wire cut machines</p>
    <div class="actions"><span class="btn">Learn More</span><span class="link-arrow">Contact <svg width="18" height="12" viewBox="0 0 18 12" fill="none" stroke="#111" stroke-width="1.4"><path d="M1 6h15M11 1l5 5-5 5"/></svg></span></div>
  </article>

  <article class="card" style="left:441px">
    <div class="photo" role="img" aria-label="Vertical CNC machining centre at work" style="background:linear-gradient(135deg,#2b4f8a,#8a7a5a,#c49a3a)"></div>
    <h3>CNC Machining: Precision at Its Finest</h3>
    <p>With our combination of high quality Hartwell Machining Centres we are able to provide innovative solutions to your precision CNC machining requirements.</p>
    <div class="actions"><span class="btn">Learn More</span><span class="link-arrow">Contact <svg width="18" height="12" viewBox="0 0 18 12" fill="none" stroke="#111" stroke-width="1.4"><path d="M1 6h15M11 1l5 5-5 5"/></svg></span></div>
  </article>

  <article class="card" style="left:797px">
    <div class="photo" role="img" aria-label="Laser metal printing nozzle in green light" style="background:linear-gradient(135deg,#4f9a1c,#8ed42a,#3e7a16)"></div>
    <h3>3D Metal Printing: Innovation in Manufacturing</h3>
    <p>Experince the future of manufacturing with our cuttin-edge 3D metal prining technology, allowing for complex geometries and efficient production.</p>
    <div class="actions"><span class="btn">Learn More</span><span class="link-arrow">Contact <svg width="18" height="12" viewBox="0 0 18 12" fill="none" stroke="#111" stroke-width="1.4"><path d="M1 6h15M11 1l5 5-5 5"/></svg></span></div>
  </article>
</section>

<section class="quality">
  <h2>Delivering quality Machined Parts with Advanced Technology</h2>
  <p class="lead">Lorem ipsum dolor sit amet, consectetur adipisicing elit, sed do eiusmod tempor incididunt ut labore et dolore magna aliqua. Ut enim ad minim veniam, quis nostrud exercitation ullamco laboris nisi ut aliquip exea comm .</p>
  <div class="stat" style="left:86px"><strong>50%</strong><p>Advanced Technology for Unmatched Precision and quality.</p>
    <div class="actions"><span class="btn">Learn More</span><span class="link-arrow">Contact <svg width="18" height="12" viewBox="0 0 18 12" fill="none" stroke="#111" stroke-width="1.4"><path d="M1 6h15M11 1l5 5-5 5"/></svg></span></div></div>
  <div class="stat" style="left:386px"><strong>50%</strong><p>Experienced Professionals Delivering Exceptional Machined Parts.</p>
    <div class="actions"><span class="btn">Learn More</span><span class="link-arrow">Contact <svg width="18" height="12" viewBox="0 0 18 12" fill="none" stroke="#111" stroke-width="1.4"><path d="M1 6h15M11 1l5 5-5 5"/></svg></span></div></div>
  <div class="photo" role="img" aria-label="Machined aluminium parts on a steel surface"></div>
</section>

<section class="cta">
  <div class="photo" role="img" aria-label="Dark close-up of a lathe and machined components"></div>
  <h2>Get a Free Quote Today</h2>
  <p>Experience Precision Machining at its Best</p>
  <div class="actions"><span class="btn btn-solid">Learn More</span><span class="btn btn-light">Contact Us</span></div>
</section>

<section class="stats">
  <h2>Delivering Excellence in machining Services</h2>
  <p class="lead">With state-of-the-art machinery and a team of skilled professionals, we have successfully completed numerous projects and achieved high client satisfaction rates.</p>
  <div class="actions"><span class="btn">Learn More</span><span class="link-arrow">Contact <svg width="18" height="12" viewBox="0 0 18 12" fill="none" stroke="#111" stroke-width="1.4"><path d="M1 6h15M11 1l5 5-5 5"/></svg></span></div>
  <div class="metric" style="left:635px;top:70px"><strong>75%</strong><span>Projects Complated</span></div>
  <div class="metric" style="left:874px;top:70px"><strong>95%</strong><span>Client Satisfaction Rate</span></div>
  <div class="metric" style="left:635px;top:202px"><strong>85%</strong><span>On-Time Delivery</span></div>
  <div class="metric" style="left:874px;top:202px"><strong>90%</strong><span>Repeat Business</span></div>
</section>

<section class="testimonial">
  <div class="photo" role="img" aria-label="Blurred dark workshop machinery"></div>
  <span class="quote-mark">“</span>
  <blockquote>I have been using their machining services for years and they always deliver&nbsp; exceptional quality. Highly recommended.</blockquote>
  <span class="arrow-btn" style="left:26px"><svg width="24" height="18" viewBox="0 0 24 18" fill="none" stroke="#fff" stroke-width="1.6"><path d="M23 9H2M9 2L2 9l7 7"/></svg></span>
  <span class="arrow-btn" style="left:1115px"><svg width="24" height="18" viewBox="0 0 24 18" fill="none" stroke="#fff" stroke-width="1.6"><path d="M1 9h21M15 2l7 7-7 7"/></svg></span>
  <div class="avatar" role="img" aria-label="Client portrait"></div>
  <div class="person"><strong>Sam Carter</strong><span>CEO, Company name</span></div>
</section>

<footer class="site-footer">
  <div class="brand"><span class="brand-name">KORVAN</span><span class="brand-mark"></span></div>
  <div class="footer-col" style="left:427px">
    <h4>OUR SERVICES</h4>
    <ul><li>EDM WIRE CUTTING</li><li>CNC MACHINING</li><li>3D METAL PRINTING</li></ul>
  </div>
  <div class="footer-col" style="left:797px">
    <h4>CONTACT US</h4>
    <address>UNIT 4,<br>18-22 FERNDALE CRT,<br>DANDRIDGE,<br>VIC 3811</address>
    <address style="margin-top:13px">TEL/FAX 03 9555 0192<br>MOB +61 400 512 874<br>EMAIL-&nbsp; info@korvanmetalworks.com.au</address>
  </div>
</footer>
<div class="copyright">Copyright © 2024 korvanmetalworks.com.au</div>

</body>
</html>
```